Finance Product Agency Business Card Design

We're an agency that provides products (service contracts, gap insurance, tire and wheel, etc) and support to dealership finance departments. We specialize in training finance producers to maximize their potential and also keep them up to date on the ever changing compliance and legal landscape. I'll attach an image of our logo, excited to see what you all come up with. Would also be interested in discussing our new website design with the winner.

Target Market(s)

auto dealerships

Industry/Entity Type

Business

Contact Information for Business Card

Mark Dolvery
Phone 317.624.5583
Fax 855.472.3308
email Mark.Dolvery@brightlanecoverage.example

Requirements
Must have
• basic contact information
Nice to have
• looking for something professional but modern

```html
<!DOCTYPE html>
<html lang="en">
<head>
<meta charset="utf-8">
<title>Brightlane Coverage — Business Card</title>
<link rel="stylesheet" href="https://fonts.googleapis.com/css2?family=Oswald:wght@600&family=Open+Sans:wght@400;600;700&display=swap">
<style>
  :root {
    --page: #e9ebec;
    --paper: #ffffff;
    --slate-deep: #1b272d;
    --slate: #2e434d;
    --slate-mid: #4a6b7b;
    --slate-soft: #8fa7b3;
    --ink-muted: #7b8a91;
    --light: #f4f7f8;
    --icon-bg: #cfd9de;
  }
  * { box-sizing: border-box; margin: 0; padding: 0; }
  html, body { width: 1200px; height: 1023px; overflow: hidden; background: var(--page); }
  body { position: relative; font-family: "Open Sans", Arial, sans-serif; }

  .card {
    position: absolute;
    width: 560px; height: 320px;
    border-radius: 4px;
    overflow: hidden;
    box-shadow: 0 10px 28px rgba(20, 30, 36, .25);
  }
  .card-art { position: absolute; left: 0; top: 0; width: 100%; height: 100%; }

  /* Front */
  .card-front { left: 60px; top: 150px; background: var(--paper); }
  .front-logo { position: absolute; left: 40px; top: 78px; display: flex; align-items: center; gap: 12px; }
  .logo-dot { width: 34px; height: 34px; border-radius: 50%; background: var(--slate-mid); }
  .logo-name {
    font-family: "Oswald", "Arial Narrow", sans-serif; font-weight: 600;
    font-size: 26px; line-height: 1.05; letter-spacing: 1px;
    color: var(--slate); text-transform: uppercase;
  }
  .person { position: absolute; left: 44px; top: 160px; }
  .person-name { font-size: 16px; font-weight: 700; color: var(--slate-mid); letter-spacing: .5px; text-transform: uppercase; }
  .person-title { font-size: 9px; color: var(--ink-muted); letter-spacing: 1px; text-transform: uppercase; margin-top: 2px; }

  .contact-list {
    position: absolute; left: 150px; top: 250px; list-style: none;
    color: var(--light); font-size: 10.5px; line-height: 1;
  }
  .contact-list li { display: flex; align-items: center; gap: 6px; height: 16px; white-space: nowrap; }
  .contact-icon { display: block; width: 10px; height: 10px; flex: none; }

  .address {
    position: absolute; right: 22px; top: 112px;
    color: var(--light); font-size: 10.5px; font-weight: 700;
    text-align: right; text-transform: uppercase; letter-spacing: .4px; line-height: 1.5;
  }

  /* Back */
  .card-back { left: 580px; top: 540px; background: linear-gradient(135deg, var(--slate) 0%, var(--slate-deep) 100%); }
  .back-logo {
    position: absolute; left: 0; right: 0; top: 118px; text-align: center;
    font-family: "Oswald", "Arial Narrow", sans-serif; font-weight: 600;
    font-size: 38px; line-height: 1.05; letter-spacing: 2px;
    color: var(--paper); text-transform: uppercase;
  }
</style>
</head>
<body>

  <section class="card card-front" aria-label="Business card front">
    <svg class="card-art" viewBox="0 0 560 320" aria-hidden="true">
      <defs>
        <linearGradient id="frontDark" x1="0" y1="0" x2="1" y2="1">
          <stop offset="0" stop-color="#3a5563"/>
          <stop offset="1" stop-color="#1b272d"/>
        </linearGradient>
      </defs>
      <path d="M0,238 C150,240 240,190 300,120 C355,55 440,12 560,4 L560,320 L0,320 Z" fill="url(#frontDark)"/>
    </svg>
    <svg class="card-art" viewBox="0 0 560 320" role="img" aria-label="Checkered flag band following the wave">
      <defs>
        <linearGradient id="checker" x1="0" y1="1" x2="1" y2="0">
          <stop offset="0" stop-color="#8fa7b3" stop-opacity=".2"/>
          <stop offset=".5" stop-color="#4a6b7b"/>
          <stop offset="1" stop-color="#1b272d"/>
        </linearGradient>
      </defs>
      <path d="M150,236 C230,215 270,170 300,120 C355,55 430,12 520,0 L470,0 C395,15 330,55 280,118 C245,160 200,205 150,236 Z" fill="url(#checker)"/>
    </svg>

    <div class="front-logo">
      <span class="logo-dot"></span>
      <span class="logo-name">Brightlane<br>Coverage</span>
    </div>
    <div class="person">
      <p class="person-name">Mark Dolvery</p>
      <p class="person-title">Director</p>
    </div>
    <ul class="contact-list">
      <li><svg class="contact-icon" viewBox="0 0 10 10" aria-hidden="true"><rect width="10" height="10" rx="1.5" fill="#cfd9de"/><path d="M3,2 L4.5,2 L5,4 L4,4.6 Q4.8,6 5.6,6.2 L6.2,5.3 L8,6 L8,7.5 Q4,8 2.5,3.5 Z" fill="#2e434d"/></svg>317.624.5583</li>
      <li><svg class="contact-icon" viewBox="0 0 10 10" aria-hidden="true"><rect width="10" height="10" rx="1.5" fill="#cfd9de"/><rect x="2.5" y="2" width="5" height="3" fill="#2e434d"/><rect x="2" y="5" width="6" height="3" fill="#2e434d"/></svg>855.472.3308</li>
      <li><svg class="contact-icon" viewBox="0 0 10 10" aria-hidden="true"><rect width="10" height="10" rx="1.5" fill="#cfd9de"/><rect x="2" y="3" width="6" height="4.2" fill="none" stroke="#2e434d" stroke-width=".9"/><path d="M2,3 L5,5.5 L8,3" fill="none" stroke="#2e434d" stroke-width=".9"/></svg>Mark.Dolvery@brightlanecoverage.example</li>
    </ul>
    <p class="address">2240 West Harlow Avenue<br>Carmel Indiana 46032</p>
  </section>

  <section class="card card-back" aria-label="Business card back">
    <svg class="card-art" viewBox="0 0 560 320" aria-hidden="true">
      <circle cx="250" cy="150" r="150" fill="#24353e" opacity=".55"/>
      <circle cx="250" cy="150" r="118" fill="none" stroke="#131c21" stroke-width="10" opacity=".7"/>
      <circle cx="250" cy="150" r="80" fill="#2b3f49" opacity=".7"/>
    </svg>
    <svg class="card-art" viewBox="0 0 560 320" role="img" aria-label="Checkered flag accents at the top right and lower left">
      <defs>
        <linearGradient id="checkerBack" x1="0" y1="0" x2="1" y2="1">
          <stop offset="0" stop-color="#5f7f8e"/>
          <stop offset="1" stop-color="#1b272d"/>
        </linearGradient>
      </defs>
      <path d="M330,0 L560,0 L560,120 C500,90 420,60 330,0 Z" fill="url(#checkerBack)" opacity=".85"/>
      <path d="M0,190 C70,215 130,250 170,320 L0,320 Z" fill="url(#checkerBack)" opacity=".85"/>
    </svg>
    <p class="back-logo">Brightlane<br>Coverage</p>
  </section>

</body>
</html>
```